Managed Service Provider VOIP Flyer

Looking for a one page US letter size single or double sided brochure to offer cloud hosted VoIP Phone system and unified communications. We have partnered with a VoIP Phone system company and want to sell their services but we don't want their name to be shown on the brochure because customers might call them directly. The company name is Quorvel (www.quorvel-example.com) and our company name is Lumen By Harlow, LLC and our voice product is called Clearly Talk. I have also uploaded my company's logo that you should show on the brochure and use that coloring. For more details about the product, you can visit their website mentioned above. Also I am looking for something very similar to this project and many of the technical details are the same https://flyer.contestpad-example.com/contest/5817264

I have also uploaded a PDF with my different package levels and some of the included features. Depending on the design we may or may not want the package levels on this flyer.

Target Market(s)

Small and medium Businesses

Industry/Entity Type

Voip

Requirements
Must have
• Feature and benefits information of Managed VOICE. Use my logo and coloring from my logo. Include our website, email, phone and possibly facebook if it makes sense/looks good.

www.lumenbyharlow-example.com
415.836.0.917
sales@lumenbyharlow-example.com
www.socialsite-example.com/lumenbyharlow
Nice to have
• Would like to show how the service is simple and reliable and available for any business size

```html
<!DOCTYPE html>
<html lang="en">
<head>
<meta charset="utf-8">
<title>Clearly Talk – Plans and Features</title>
<link href="https://fonts.googleapis.com/css2?family=Montserrat:wght@400;500;600;700&family=Roboto+Condensed:wght@700&display=swap" rel="stylesheet">
<style>
:root{
  --navy:#1f2262;
  --navy-deep:#0f1139;
  --navy-mid:#272b78;
  --red:#b41e24;
  --red-deep:#7c0b0f;
  --grey-row:#ebebeb;
  --ink:#1d1d1d;
  --muted:#333;
  --bg:#e7e4e0;
}
*{box-sizing:border-box;margin:0;padding:0}
html,body{width:1200px;height:1200px;overflow:hidden}
body{background:var(--bg);font-family:"Montserrat",Arial,sans-serif;color:var(--ink);position:relative}

.page{position:absolute;top:214px;width:552px;height:772px;background:#fff;overflow:hidden;box-shadow:0 2px 6px rgba(0,0,0,.18)}
.page--plans{left:31px}
.page--features{left:616px}

.header{position:relative;height:93px;background:var(--navy)}
.header__logo-panel{position:absolute;left:0;top:16px;width:215px;height:77px;background:#fff;border-top-right-radius:42px;display:flex;align-items:center;padding-left:22px;gap:10px}
.logo-dot{width:30px;height:30px;border-radius:50%;background:var(--red);flex:none}
.logo-name{font-weight:600;font-size:17px;line-height:1.05;color:var(--navy)}
.header__art{position:absolute;left:222px;top:4px;width:150px;height:86px;border-radius:6px;background:radial-gradient(ellipse at 40% 55%,#3c4aa6 0%,#2a3286 40%,rgba(31,34,98,0) 75%)}
.header__contact{position:absolute;right:36px;top:20px;text-align:right;color:#fff}
.contact__company{font-size:8.5px;margin-bottom:6px}
.contact__phone{font-size:13px;font-weight:500;margin-bottom:8px;display:flex;align-items:center;justify-content:flex-end;gap:5px}
.contact__email{font-size:8.5px;display:flex;align-items:center;justify-content:flex-end;gap:5px}

.footer{position:absolute;left:0;bottom:0;width:100%;height:38px;background:var(--red);color:#fff;display:flex;align-items:center;justify-content:space-between;padding:0 20px 0 22px;font-size:8.6px}
.footer__tag{font-weight:600}
.footer__link{display:flex;align-items:center;gap:5px}
.footer__dot{width:8px;height:8px;border-radius:50%;background:#fff;flex:none}

.plan-table{position:absolute;left:8px;top:93px;width:536px;display:grid;grid-template-columns:187px 114px 115px 114px;column-gap:2px}
.th{height:30px;display:flex;align-items:center;justify-content:center;color:#fff;font-weight:600;font-size:10.5px;letter-spacing:.2px}
.th--plan{background:var(--red-deep)}
.th--tier{background:var(--navy-deep)}
.price{height:72px;display:flex;flex-direction:column;align-items:center;justify-content:center;color:#fff}
.price--label{background:var(--red);font-weight:700;font-size:23px;line-height:1.2;text-align:center}
.price--tier{background:var(--navy-mid)}
.price__note{font-size:9px;opacity:.9;margin-bottom:4px}
.price__amount{font-size:28px;font-weight:700;line-height:1}
.price__amount sup{font-size:15px;vertical-align:10px;margin-right:1px}
.cell{height:21.4px;display:flex;align-items:center;font-size:9.5px;color:var(--ink)}
.cell--label{padding-left:8px}
.cell--val{justify-content:center}
.cell--tall{height:42.8px;line-height:1.15}
.row-alt{background:var(--grey-row)}
.first-row{margin-top:4px}

.columns{position:absolute;left:0;top:93px;width:100%;height:641px}
.col-seat{position:absolute;left:0;top:0;width:274px;height:100%;background:#fff;padding:0 20px 0 22px}
.col-pbx{position:absolute;left:274px;top:0;width:278px;height:100%;background:#e6e6e6;padding:0 20px 0 22px}
.tab{position:relative;color:#fff;font-family:"Roboto Condensed","Arial Narrow",sans-serif;font-weight:700;text-transform:uppercase;display:flex;align-items:center;gap:8px;padding-left:12px;clip-path:polygon(0 0,100% 0,100% calc(100% - 8px),92% calc(100% - 8px),88% 100%,84% calc(100% - 8px),0 calc(100% - 8px))}
.tab--seat{margin-left:-4px;width:240px;height:38px;font-size:16px;padding-bottom:8px;background:var(--red)}
.tab--pbx{margin-left:-2px;width:240px;height:56px;font-size:15px;line-height:1.05;padding-bottom:8px;background:var(--red);margin-bottom:12px}
.tab--addon{margin-left:-2px;width:240px;height:38px;font-size:16px;padding-bottom:8px;background:var(--red);margin-top:20px;margin-bottom:12px}
.tab__icon{width:14px;height:16px;border:2px solid #fff;border-radius:2px;flex:none}
.tab__rule{width:1.5px;height:22px;background:#fff;flex:none}
.seat-list{height:585px;margin-top:10px;display:flex;flex-direction:column;justify-content:space-between}
.feature__title{display:flex;align-items:center;gap:4px;font-size:9.6px;font-weight:500;color:var(--ink);margin-bottom:3px}
.feature__desc{font-size:6.6px;line-height:1.3;color:var(--muted);text-align:justify}
.pbx-list .feature{margin-bottom:16px}
.pbx-list--addon .feature{margin-bottom:22px}
.warn{flex:none}
</style>
</head>
<body>

<svg width="0" height="0" style="position:absolute">
  <defs>
    <symbol id="warn" viewBox="0 0 10 9"><path d="M5 0 L10 9 L0 9 Z" fill="#b41e24"/><rect x="4.4" y="3" width="1.2" height="3.2" fill="#fff"/><rect x="4.4" y="6.9" width="1.2" height="1.1" fill="#fff"/></symbol>
    <symbol id="phone" viewBox="0 0 10 16"><path d="M3 1 Q1 1 1 4 Q1 10 6 15 Q8 15 9 13 L7 10 Q6 11 5 11 Q3 8 3 5 Q4 5 5 4 L4 1 Z" fill="#fff"/></symbol>
    <symbol id="mail" viewBox="0 0 16 11"><rect x=".5" y=".5" width="15" height="10" fill="#fff"/><path d="M.5 .5 L8 6 L15.5 .5" fill="none" stroke="#1f2262" stroke-width="1"/></symbol>
  </defs>
</svg>

<section class="page page--plans">
  <header class="header">
    <div class="header__logo-panel"><span class="logo-dot"></span><span class="logo-name">Lumen By<br>Harlow</span></div>
    <div class="header__art" role="img" aria-label="Illustration of a person working at a computer desk surrounded by communication icons"></div>
    <div class="header__contact">
      <div class="contact__company">Lumen By Harlow, LLC</div>
      <div class="contact__phone">+1 (415) 836-0917 <svg width="8" height="13"><use href="#phone"/></svg></div>
      <div class="contact__email">sales@lumenbyharlow-example.com <svg width="14" height="10"><use href="#mail"/></svg></div>
    </div>
  </header>

  <div class="plan-table">
    <div class="th th--plan">PLAN</div><div class="th th--tier">PRIMER</div><div class="th th--tier">STANDARD</div><div class="th th--tier">PREMIUM</div>
    <div class="price price--label">MONTHLY<br>PRICE</div>
    <div class="price price--tier"><span class="price__note">(Location, not a user)</span><span class="price__amount"><sup>$</sup>20</span></div>
    <div class="price price--tier"><span class="price__note">(Basic user)</span><span class="price__amount"><sup>$</sup>30</span></div>
    <div class="price price--tier"><span class="price__note">(Power user)</span><span class="price__amount"><sup>$</sup>35</span></div>

    <div class="cell cell--label first-row">Extension Dialing</div><div class="cell cell--val first-row row-alt">Yes</div><div class="cell cell--val first-row row-alt">Yes</div><div class="cell cell--val first-row row-alt">Yes</div>
    <div class="cell cell--label row-alt">Local Outbound Calls Only</div><div class="cell cell--val">Yes</div><div class="cell cell--val">LD Included</div><div class="cell cell--val">LD Included</div>
    <div class="cell cell--label">Caller ID and Caller Name Delivery</div><div class="cell cell--val row-alt">Yes</div><div class="cell cell--val row-alt">Yes</div><div class="cell cell--val row-alt">Yes</div>
    <div class="cell cell--label row-alt">Call Logs</div><div class="cell cell--val">Yes</div><div class="cell cell--val">Yes</div><div class="cell cell--val">Yes</div>
    <div class="cell cell--label">Last Number Redia</div><div class="cell cell--val row-alt">Yes (Local Only)</div><div class="cell cell--val row-alt">Yes</div><div class="cell cell--val row-alt">Yes</div>
    <div class="cell cell--label row-alt">Music On Hold</div><div class="cell cell--val">Yes</div><div class="cell cell--val">Yes</div><div class="cell cell--val">Yes</div>
    <div class="cell cell--label">Corporate Directory Access</div><div class="cell cell--val row-alt">Yes</div><div class="cell cell--val row-alt">Yes</div><div class="cell cell--val row-alt">Yes</div>
    <div class="cell cell--label row-alt">E911 Service</div><div class="cell cell--val">Yes</div><div class="cell cell--val">Yes</div><div class="cell cell--val">Yes</div>
    <div class="cell cell--label">E911 Service</div><div class="cell cell--val row-alt">No</div><div class="cell cell--val row-alt">yes</div><div class="cell cell--val row-alt">yes</div>
    <div class="cell cell--label row-alt">Call Park</div><div class="cell cell--val">No</div><div class="cell cell--val">yes</div><div class="cell cell--val">yes</div>
    <div class="cell cell--label cell--tall">Call Forwarding<br>(Always, Busy, No-Answer,<br>Not Reachable)</div><div class="cell cell--val cell--tall row-alt">No</div><div class="cell cell--val cell--tall row-alt">yes</div><div class="cell cell--val cell--tall row-alt">yes</div>
    <div class="cell cell--label row-alt">Call Recording</div><div class="cell cell--val">No</div><div class="cell cell--val">Additional</div><div class="cell cell--val">Additional</div>
    <div class="cell cell--label">Call Transfer</div><div class="cell cell--val row-alt">No</div><div class="cell cell--val row-alt">Yes</div><div class="cell cell--val row-alt">Yes</div>
    <div class="cell cell--label row-alt">Call Waiting</div><div class="cell cell--val">No</div><div class="cell cell--val">Yes</div><div class="cell cell--val">Yes</div>
    <div class="cell cell--label">Unified Messaging</div><div class="cell cell--val row-alt">No</div><div class="cell cell--val row-alt">Yes</div><div class="cell cell--val row-alt">Yes</div>
    <div class="cell cell--label row-alt">Inclusion in Hunt Groups</div><div class="cell cell--val">No</div><div class="cell cell--val">Yes</div><div class="cell cell--val">Yes</div>
    <div class="cell cell--label">Simultaneous Ring</div><div class="cell cell--val row-alt">No</div><div class="cell cell--val row-alt">Yes</div><div class="cell cell--val row-alt">Yes</div>
    <div class="cell cell--label row-alt">Sequential Ring</div><div class="cell cell--val">No</div><div class="cell cell--val">Yes</div><div class="cell cell--val">Yes</div>
    <div class="cell cell--label">Speed Dial 100</div><div class="cell cell--val row-alt">No</div><div class="cell cell--val row-alt">Yes</div><div class="cell cell--val row-alt">Yes</div>
    <div class="cell cell--label row-alt">Three-Way Calling</div><div class="cell cell--val">No</div><div class="cell cell--val"></div><div class="cell cell--val">Yes</div>
    <div class="cell cell--label">Connect Client</div><div class="cell cell--val row-alt">No</div><div class="cell cell--val row-alt"></div><div class="cell cell--val row-alt">Yes</div>
    <div class="cell cell--label row-alt">Desktop Sharing</div><div class="cell cell--val">No</div><div class="cell cell--val"></div><div class="cell cell--val">Yes</div>
    <div class="cell cell--label">Web Collaboration</div><div class="cell cell--val row-alt">No</div><div class="cell cell--val row-alt"></div><div class="cell cell--val row-alt">Yes</div>
  </div>

  <footer class="footer">
    <span class="footer__tag">Simple Voice, Steady Business</span>
    <span class="footer__link"><span class="footer__dot"></span>www.socialsite-example.com/lumenbyharlow</span>
    <span class="footer__link"><span class="footer__dot"></span>www.lumenbyharlow-example.com</span>
  </footer>
</section>

<section class="page page--features">
  <header class="header">
    <div class="header__logo-panel"><span class="logo-dot"></span><span class="logo-name">Lumen By<br>Harlow</span></div>
    <div class="header__art" role="img" aria-label="Illustration of a person working at a computer desk surrounded by communication icons"></div>
    <div class="header__contact">
      <div class="contact__company">Lumen By Harlow, LLC</div>
      <div class="contact__phone">+1 (415) 836-0917 <svg width="8" height="13"><use href="#phone"/></svg></div>
      <div class="contact__email">sales@lumenbyharlow-example.com <svg width="14" height="10"><use href="#mail"/></svg></div>
    </div>
  </header>

  <div class="columns">
    <div class="col-seat">
      <div class="tab tab--seat"><span class="tab__icon"></span><span class="tab__rule"></span>Seat Features</div>
      <div class="seat-list">
        <div class="feature"><div class="feature__title"><svg class="warn" width="10" height="9"><use href="#warn"/></svg>3-Way Calling</div><p class="feature__desc">With a 3-Way Call, or an ad-hoc conference, you can bring two other lines (internal and/or external) into a call with you.</p></div>
        <div class="feature"><div class="feature__title"><svg class="warn" width="10" height="9"><use href="#warn"/></svg>Call Logs</div><p class="feature__desc">Your administrator will have access to view call detail records, such as inbound and outbound calls, time, and duration.</p></div>
        <div class="feature"><div class="feature__title"><svg class="warn" width="10" height="9"><use href="#warn"/></svg>Caller ID and Caller Name Delivery</div><p class="feature__desc">Incoming calls will include the incoming caller ID and caller name if provided by the network.</p></div>
        <div class="feature"><div class="feature__title"><svg class="warn" width="10" height="9"><use href="#warn"/></svg>Call Waiting</div><p class="feature__desc">Call waiting allows you to receive a new call while you are still on an existing call.</p></div>
        <div class="feature"><div class="feature__title"><svg class="warn" width="10" height="9"><use href="#warn"/></svg>Call Forward Always</div><p class="feature__desc">Forward all incoming calls to another extension or phone number.</p></div>
        <div class="feature"><div class="feature__title"><svg class="warn" width="10" height="9"><use href="#warn"/></svg>Call Forward Busy</div><p class="feature__desc">Forward incoming calls to another extension or phone number when your phone is busy or in Do Not Disturb mode.</p></div>
        <div class="feature"><div class="feature__title"><svg class="warn" width="10" height="9"><use href="#warn"/></svg>Call Forward No Answer</div><p class="feature__desc">Forward unanswered calls to an extension or phone number other than the voicemail after a set number of rings (default 3).</p></div>
        <div class="feature"><div class="feature__title"><svg class="warn" width="10" height="9"><use href="#warn"/></svg>Call Forward Not Reachable</div><p class="feature__desc">In the event that you lose your internet service, you can set a number to forward calls to when your phone is offline.</p></div>
        <div class="feature"><div class="feature__title"><svg class="warn" width="10" height="9"><use href="#warn"/></svg>Do Not Disturb</div><p class="feature__desc">Placing your phone service in Do Not Disturb will cause all calls to go to your voicemail box or specified busy treatment.</p></div>
        <div class="feature"><div class="feature__title"><svg class="warn" width="10" height="9"><use href="#warn"/></svg>Extension Dialing</div><p class="feature__desc">You may call other phones in your PBX with an extension, even if they are in other locations.</p></div>
        <div class="feature"><div class="feature__title"><svg class="warn" width="10" height="9"><use href="#warn"/></svg>Last Number Redial</div><p class="feature__desc">You can redial the last number you called.</p></div>
        <div class="feature"><div class="feature__title"><svg class="warn" width="10" height="9"><use href="#warn"/></svg>Simultaneous Ring</div><p class="feature__desc">You can specify extensions and numbers to ring at the same time as the desk line extension.</p></div>
        <div class="feature"><div class="feature__title"><svg class="warn" width="10" height="9"><use href="#warn"/></svg>Sequential Ring</div><p class="feature__desc">A sequence of extensions and numbers can be set up to dial if the desk phone does not pick up</p></div>
        <div class="feature"><div class="feature__title"><svg class="warn" width="10" height="9"><use href="#warn"/></svg>Speed Dial 100</div><p class="feature__desc">You can specify up to 100 number to dial with #xx with the dial pad</p></div>
        <div class="feature"><div class="feature__title"><svg class="warn" width="10" height="9"><use href="#warn"/></svg>Unified Messaging</div><p class="feature__desc">Your seat has voicemail included, but can also be configured for voicemail to email, zero-out, and email notifications.</p></div>
      </div>
    </div>

    <div class="col-pbx">
      <div class="tab tab--pbx"><span class="tab__icon"></span><span class="tab__rule"></span><span>All PBX include the<br>following features</span></div>
      <div class="pbx-list">
        <div class="feature"><div class="feature__title"><svg class="warn" width="10" height="9"><use href="#warn"/></svg>Auto Attendant</div><p class="feature__desc">An automated recording that answers the phone and provides a personalized message to callers with options for connecting to the operator, dialing by name or extension, or connecting to up to nine configurable extensions. Configuration via the Customer Portal allows for hours of operation to be modified, with different options available for hours that the company is open or closed.</p></div>
        <div class="feature"><div class="feature__title"><svg class="warn" width="10" height="9"><use href="#warn"/></svg>Company Main Number</div><p class="feature__desc">Phone number with unlimited incoming minutes that can be configured to point to any group extension in the PBX (such as an auto attendant or hunt group).</p></div>
        <div class="feature"><div class="feature__title"><svg class="warn" width="10" height="9"><use href="#warn"/></svg>Corporate Directory</div><p class="feature__desc">System Users are networked for extension to extension calling.</p></div>
        <div class="feature"><div class="feature__title"><svg class="warn" width="10" height="9"><use href="#warn"/></svg>Hunt Groups</div><p class="feature__desc">Allows users within a group to be included in a specified subgroup to handle incoming calls received by an assigned Hunt Group's phone number. Within the Customer Portal, company administrators can choose from "hunt" schemes, each of which rings the specified phones in a different manner.</p></div>
        <div class="feature"><div class="feature__title"><svg class="warn" width="10" height="9"><use href="#warn"/></svg>Music on Hold</div><p class="feature__desc">Enables company administrators to upload an audio file (.wav file containing music, advertising, etc.) onto the system to be broadcast to parties while on hold.</p></div>
      </div>
      <div class="tab tab--addon"><span class="tab__icon"></span><span class="tab__rule"></span>Add-On Features</div>
      <div class="pbx-list pbx-list--addon">
        <div class="feature"><div class="feature__title"><svg class="warn" width="10" height="9"><use href="#warn"/></svg>Advanced Auto Attendant</div><p class="feature__desc">A multi-level Auto Attendant (for example, enterprise's main Auto Attendant is configured to seamlessly route to the Auto Attendant of a particular department or location).</p></div>
        <div class="feature"><div class="feature__title"><svg class="warn" width="10" height="9"><use href="#warn"/></svg>Call Recording</div><p class="feature__desc">Allows a user to record their calls in either an always on or ondemand mode. These recording capabilities can allow for personal monitoring or supervised monitoring of recorded calls.</p></div>
        <div class="feature"><div class="feature__title"><svg class="warn" width="10" height="9"><use href="#warn"/></svg>Toll-Free Numbers</div><p class="feature__desc">An "800" number with inbound calling charged a toll to you, not the caller.</p></div>
        <div class="feature"><div class="feature__title"><svg class="warn" width="10" height="9"><use href="#warn"/></svg>Virtual Number</div><p class="feature__desc">Additional phone number with unlimited incoming minutes that can be configured to point to any extension in the PBX.</p></div>
      </div>
    </div>
  </div>

  <footer class="footer">
    <span class="footer__tag">Simple Voice, Steady Business</span>
    <span class="footer__link"><span class="footer__dot"></span>www.socialsite-example.com/lumenbyharlow</span>
    <span class="footer__link"><span class="footer__dot"></span>www.lumenbyharlow-example.com</span>
  </footer>
</section>

</body>
</html>
```